Neues Corporate Design für Steuerberaterin
Zielgruppe
Ich bin seit Kurzem als Steuerberaterin selbständig tätig. Meine Zielgruppe sind v.a. junge engagierte Leute zwischen 25 und 45 Jahren - Privatpersonen als auch Unternehmer - die ein bisschen anders denken und sich beim herkömmlichen Steuerberater nicht gut aufgehoben fühlen. Mir ist auch der persönliche/menschliche Aspekt mit meinen Kunden sehr wichtig (im Gegensatz zu vielen anderen), denn fachlich top sind eh die meisten und mein Eindruck ist, das alleine reicht nicht mehr aus.
Aufgabenstellung
Ich habe mich in den vergangenen Jahren bereits ein bisschen auf die Selbständigkeit vorbereitet und u.a. auch eine Visitenkarte entworfen (siehe Anhang). Allerdings ist das schon etwas länger her und ich finde diese 'alte' Visitenkarte nicht mehr ganz zeitgemäß bzw. auch zu undurchdacht. Das Logo (Weintraube und Paragraph) finde ich auch nicht mehr so passend (und etwas unseriös). Mir wär lieber ein schönen Schriftzug oder ein Logo mit Initialen oder sonst etwas Kreatives, damit das Ganze etwas professioneller wirkt. Meine Lieblingsfarbe ist violett, es kann aber auch gerne hell und dunkel gemischt werden. Ich könnte mir ebenfalls ein Farbspiel mit Kreisen oder Ecken oder sonst etwas vorstellen. Auf der Vorderseite der Visitenkarte hätte ich gerne 'Lena Moosbrugger - Steuerberatung' stehen. Auf der Rückseite dann 'Steuerberaterin MMag. Lena Moosbrugger' und alle Informationen die auch im Anhang zu finden sind. Ganz unten sollen graphisch abgegrenzt beiden Büro-Adressen stehen. So zumindest mal mein Vorschlag, bin aber auch für andere Ideen offen.

```html
<!DOCTYPE html>
<html lang="de">
<head>
<meta charset="utf-8">
<title>Lena Moosbrugger – Corporate Design</title>
<link rel="stylesheet" href="https://fonts.googleapis.com/css2?family=Playfair+Display:wght@400&family=Arimo:wght@400&display=swap">
<style>
  :root {
    --light: #ad76aa;
    --dark: #7a4f8c;
    --ink: #1e1e1e;
    --paper: #ffffff;
    --shadow: 0 0 3px rgba(0,0,0,.28);
    --serif: "Playfair Display", Georgia, serif;
    --sans: "Arimo", Arial, sans-serif;
  }
  * { box-sizing: border-box; margin: 0; padding: 0; }
  html, body { width: 1200px; height: 1200px; overflow: hidden; background: var(--paper); }
  .canvas { position: relative; width: 1200px; height: 1200px; }

  /* wordmark variants */
  .mark-row { position: absolute; top: 50px; left: 0; width: 1200px; height: 112px; }
  .wordmark {
    position: absolute; top: 0; width: 108px; height: 108px;
    border: 1px solid var(--light); border-radius: 50%;
    display: flex; align-items: center; justify-content: center; text-align: center;
    font-family: var(--serif); color: var(--dark); font-size: 13px; line-height: 1.25;
  }

  /* stationery set */
  .set { position: absolute; left: 0; width: 1200px; height: 420px; }
  .set--light { top: 253px; --accent: var(--light); }
  .set--dark  { top: 766px; --accent: var(--dark); }

  .letter {
    position: absolute; left: 256px; top: 0; width: 292px; height: 419px;
    background: var(--paper); box-shadow: var(--shadow);
  }
  .frame {
    position: absolute; border: 1px solid var(--accent);
  }
  .frame__label {
    position: absolute; left: 50%; bottom: -5px; transform: translateX(-50%);
    background: inherit; padding: 0 3px; white-space: nowrap;
    font-family: var(--serif); font-size: 7.5px; letter-spacing: .2px; color: var(--accent);
    line-height: 9px;
  }
  .emblem {
    position: absolute; left: 50%; transform: translateX(-50%);
    border: 1px solid var(--light); border-radius: 50%;
    display: flex; align-items: center; justify-content: center; text-align: center;
    font-family: var(--serif); color: var(--dark); line-height: 1.2;
  }
  .letter .frame { left: 11px; top: 14px; width: 268px; height: 61px; background: var(--paper); }
  .letter .emblem { top: 12px; width: 40px; height: 40px; font-size: 5px; }
  .letter__body { position: absolute; left: 11px; top: 124px; width: 247px; font-family: var(--sans); color: var(--ink); }
  .letter__salutation { font-size: 5.4px; margin-bottom: 19px; }
  .letter__body p { font-size: 5.1px; line-height: 9px; text-align: justify; margin-bottom: 8.6px; }
  .signature { position: absolute; left: 11px; top: 280px; width: 63px; height: 38px; background: #ececec; }
  .letter__signee { position: absolute; left: 11px; top: 326px; font-family: var(--sans); font-size: 5.4px; color: var(--ink); }
  .letter__footer {
    position: absolute; left: 0; bottom: 0; width: 100%; height: 42px; background: var(--accent);
    color: #f3e9f2; font-family: var(--sans); font-size: 4.6px; line-height: 8.5px;
    display: flex; justify-content: space-between; padding: 4px 14px 0 11px;
  }
  .letter__footer .offices { text-align: right; padding-top: 3px; line-height: 6.2px; }
  .letter__footer .offices span { display: block; margin-bottom: 2.6px; }

  /* business cards */
  .card {
    position: absolute; width: 178px; height: 131px; background: var(--paper); box-shadow: var(--shadow);
  }
  .card--a { left: 561px; top: 0; background: var(--accent); }
  .card--b { left: 750px; top: 0; background: var(--accent); }
  .card--c { left: 561px; top: 246px; }
  .card--d { left: 750px; top: 246px; }

  .card--a .frame { left: 5px; top: 6px; right: 5px; bottom: 7px; border-color: rgba(255,255,255,.8); background: var(--accent); }
  .card--a .frame__label { color: #fff; }
  .card--a .emblem { top: 26px; width: 68px; height: 68px; border-color: #fff; color: #fff; font-size: 8px; }

  .card--b .inner { position: absolute; left: 6px; top: 6px; right: 6px; bottom: 6px; background: var(--paper); }
  .card--b .frame { left: 4px; top: 4px; right: 4px; bottom: 6px; background: var(--paper); }
  .card--b .emblem { top: 18px; width: 62px; height: 62px; font-size: 7.5px; }

  .card--c .frame { left: 5px; top: 6px; right: 5px; bottom: 7px; background: var(--paper); }
  .card--c .emblem { top: 26px; width: 68px; height: 68px; font-size: 8px; }

  .card--d .frame { left: 7px; top: 6px; right: 7px; height: 46px; background: var(--paper); }
  .card--d .frame__label { font-size: 5px; letter-spacing: .4px; bottom: -4px; line-height: 7px; }
  .card--d .emblem { top: 6px; width: 26px; height: 26px; font-size: 3.6px; }
  .card__name {
    position: absolute; top: 62px; width: 100%; text-align: center;
    font-family: var(--serif); font-size: 5.5px; color: var(--accent); font-variant: small-caps; letter-spacing: .2px;
  }
  .card__contact {
    position: absolute; top: 79px; width: 100%; text-align: center;
    font-family: var(--sans); font-size: 3.8px; color: #8e8e8e; line-height: 5.4px;
  }
  .card__contact .gap { display: block; height: 3.6px; }
  .card__footer {
    position: absolute; left: 0; bottom: 0; width: 100%; height: 22px; background: var(--accent);
    color: #f3e9f2; font-family: var(--sans); font-size: 3.3px; line-height: 4.8px;
    display: flex; justify-content: space-between; align-items: center; padding: 0 7px;
  }
  .card__footer div:last-child { text-align: right; }
</style>
</head>
<body>
<main class="canvas">

  <section class="mark-row" aria-label="Wortmarken-Varianten">
    <div class="wordmark" style="left:375px">Lena<br>Moosbrugger</div>
    <div class="wordmark" style="left:541px">Lena<br>Moosbrugger</div>
    <div class="wordmark" style="left:705px">Lena<br>Moosbrugger</div>
  </section>

  <section class="set set--light" aria-label="Geschäftsausstattung hell">
    <article class="letter">
      <div class="frame">
        <div class="emblem">Lena<br>Moosbrugger</div>
        <span class="frame__label">LENA MOOSBRUGGER</span>
      </div>
      <div class="letter__body">
        <div class="letter__salutation">DEAR BERGER,</div>
        <p>Lorem ipsum dolor sit amet, consectetuer adipiscing elit, sed diam nonummy nibh euismod tincidunt ut laoreet dolore magna aliquam erat volutpat. Ut wisi enim ad minim veniam, quis nostrud exerci tation ullamcorper suscipit lobortis nisl ut aliquip ex ea commodo consequat.</p>
        <p>Duis autem vel eum iriure dolor in hendrerit in vulputate velit esse molestie consequat, vel illum dolore eu feugiat nulla facilisis at vero eros et accumsan et iusto odio dignissim qui blandit praesent luptatum zzril delenit augue duis dolore te feugait nulla facilisi.</p>
        <p>Lorem ipsum dolor sit amet, cons ectetuer adipiscing elit, sed diam nonummy nibh euismod tincidunt ut laoreet dolore magna aliquam erat volutpat. Ut wisi enim ad minim veniam, quis nostrud exerci tation ullamcorper suscipit lobortis nisl ut aliquip ex ea commodo consequat.</p>
      </div>
      <div class="signature" role="img" aria-label="Handschriftliche Unterschrift"></div>
      <div class="letter__signee">Lena Moosbrugger</div>
      <footer class="letter__footer">
        <div>Mobil: +43 660 12 34 567<br>E-Mail: office@kanzlei-moosbrugger.at<br>Web: www.kanzlei-moosbrugger.at<br>UID: AT...</div>
        <div class="offices"><span>BÜRO STEIERMARK:<br>Birkenweg 7, 8530 Deutschlandsberg</span><span>BÜRO WIEN:<br>Lindengasse 12, 1070 Wien</span></div>
      </footer>
    </article>

    <article class="card card--a">
      <div class="frame"><div class="emblem">Lena<br>Moosbrugger</div><span class="frame__label">LENA MOOSBRUGGER</span></div>
    </article>
    <article class="card card--b">
      <div class="inner"><div class="frame"><div class="emblem">Lena<br>Moosbrugger</div><span class="frame__label">LENA MOOSBRUGGER</span></div></div>
    </article>
    <article class="card card--c">
      <div class="frame"><div class="emblem">Lena<br>Moosbrugger</div><span class="frame__label">LENA MOOSBRUGGER</span></div>
    </article>
    <article class="card card--d">
      <div class="frame"><div class="emblem">Lena<br>Moosbrugger</div><span class="frame__label">STEUERBERATERIN</span></div>
      <div class="card__name">MMag. Lena Moosbrugger, LL.M.</div>
      <div class="card__contact">Mobil: +43 660 12 34 567<span class="gap"></span>E-Mail: office@kanzlei-moosbrugger.at<br>Web: www.kanzlei-moosbrugger.at</div>
      <footer class="card__footer"><div>BÜRO STEIERMARK:<br>Birkenweg 7, 8530 Deutschlandsberg</div><div>BÜRO WIEN:<br>Lindengasse 12, 1070 Wien</div></footer>
    </article>
  </section>

  <section class="set set--dark" aria-label="Geschäftsausstattung dunkel">
    <article class="letter">
      <div class="frame">
        <div class="emblem">Lena<br>Moosbrugger</div>
        <span class="frame__label" style="color:var(--light)">LENA MOOSBRUGGER</span>
      </div>
      <div class="letter__body">
        <div class="letter__salutation">DEAR BERGER,</div>
        <p>Lorem ipsum dolor sit amet, consectetuer adipiscing elit, sed diam nonummy nibh euismod tincidunt ut laoreet dolore magna aliquam erat volutpat. Ut wisi enim ad minim veniam, quis nostrud exerci tation ullamcorper suscipit lobortis nisl ut aliquip ex ea commodo consequat.</p>
        <p>Duis autem vel eum iriure dolor in hendrerit in vulputate velit esse molestie consequat, vel illum dolore eu feugiat nulla facilisis at vero eros et accumsan et iusto odio dignissim qui blandit praesent luptatum zzril delenit augue duis dolore te feugait nulla facilisi.</p>
        <p>Lorem ipsum dolor sit amet, cons ectetuer adipiscing elit, sed diam nonummy nibh euismod tincidunt ut laoreet dolore magna aliquam erat volutpat. Ut wisi enim ad minim veniam, quis nostrud exerci tation ullamcorper suscipit lobortis nisl ut aliquip ex ea commodo consequat.</p>
      </div>
      <div class="signature" role="img" aria-label="Handschriftliche Unterschrift"></div>
      <div class="letter__signee">Lena Moosbrugger</div>
      <footer class="letter__footer">
        <div>Mobil: +43 660 12 34 567<br>E-Mail: office@kanzlei-moosbrugger.at<br>Web: www.kanzlei-moosbrugger.at<br>UID: AT...</div>
        <div class="offices"><span>BÜRO STEIERMARK:<br>Birkenweg 7, 8530 Deutschlandsberg</span><span>BÜRO WIEN:<br>Lindengasse 12, 1070 Wien</span></div>
      </footer>
    </article>

    <article class="card card--a">
      <div class="frame"><div class="emblem">Lena<br>Moosbrugger</div><span class="frame__label">LENA MOOSBRUGGER</span></div>
    </article>
    <article class="card card--b">
      <div class="inner"><div class="frame"><div class="emblem">Lena<br>Moosbrugger</div><span class="frame__label" style="color:var(--light)">LENA MOOSBRUGGER</span></div></div>
    </article>
    <article class="card card--c">
      <div class="frame" style="border-color:var(--light)"><div class="emblem">Lena<br>Moosbrugger</div><span class="frame__label" style="color:var(--light)">LENA MOOSBRUGGER</span></div>
    </article>
    <article class="card card--d">
      <div class="frame" style="border-color:var(--light)"><div class="emblem">Lena<br>Moosbrugger</div><span class="frame__label" style="color:var(--light)">STEUERBERATERIN</span></div>
      <div class="card__name" style="color:var(--light)">MMag. Lena Moosbrugger, LL.M.</div>
      <div class="card__contact">Mobil: +43 660 12 34 567<span class="gap"></span>E-Mail: office@kanzlei-moosbrugger.at<br>Web: www.kanzlei-moosbrugger.at</div>
      <footer class="card__footer"><div>BÜRO STEIERMARK:<br>Birkenweg 7, 8530 Deutschlandsberg</div><div>BÜRO WIEN:<br>Lindengasse 12, 1070 Wien</div></footer>
    </article>
  </section>

</main>
</body>
</html>
```